Award-winnning Estate Agent needs a premium version of their 'For Sale' board design

We need a premium option for our 'For Sale' board design. We have a standard board that is attached to this brief, but were are looking to have a premium design version that we will use when selling exclusive properties. Our company name is Harbour Lane Estates and the name for this is exclusive selection is: 'The Harbour Collection'. The design needs to work with our current brand, but have a distinctive PREMIUM feel to it. I have uploaded the barnd guidelines and also some of the exisisting logo variations. We do NOT need a new logo but feel free to play around with colours, fonts, sizes etc. for the sign.

Target Market(s)

Property buyers & house hunters

Industry/Entity Type

Real Estate - Residential Property

Font styles to use
Sans Serif

Requirements
Must have
• A premium fee, must be square design, must be easy to read when driving past the sign
Nice to have
• I'm open ot ideas

```html
<!DOCTYPE html>
<html lang="en">
<head>
<meta charset="utf-8">
<title>Harbour Lane Estates – For Sale Board</title>
<link rel="stylesheet" href="https://fonts.googleapis.com/css2?family=Montserrat:wght@500;700;800&family=Cinzel:wght@500&family=Tinos&display=swap">
<style>
  :root {
    --page: #efefef;
    --black: #000000;
    --black-soft: #2a2a2a;
    --white: #ffffff;
    --gold: #c0a031;
    --gold-light: #e6cb6a;
    --gold-deep: #7a5d0f;
    --ink: #3a3a3a;
    --panel-top: #f4f4f4;
    --panel-bottom: #e4dcc8;
  }
  * { margin: 0; padding: 0; box-sizing: border-box; }
  html, body {
    width: 1200px; height: 672px; overflow: hidden;
    background: var(--page);
  }
  .canvas {
    width: 1200px; height: 672px;
    display: flex; align-items: center; justify-content: center;
  }
  .board {
    position: relative;
    width: 600px; height: 600px;
    display: flex; flex-direction: column;
    box-shadow: 0 14px 18px -10px rgba(0,0,0,0.45);
  }
  .board__header {
    height: 134px;
    background: radial-gradient(ellipse at 60% 0%, var(--black-soft) 0%, var(--black) 60%);
    display: flex; align-items: center; justify-content: center;
  }
  .board__headline {
    font-family: "Montserrat", sans-serif;
    font-weight: 800;
    font-size: 94px;
    letter-spacing: -1px;
    color: var(--white);
    line-height: 1;
    padding-top: 6px;
  }
  .board__rule {
    height: 13px;
    background: var(--gold);
  }
  .board__body {
    position: relative;
    flex: 1;
    background: linear-gradient(180deg, var(--panel-top) 0%, #ececec 45%, var(--panel-bottom) 100%);
    display: flex; flex-direction: column; align-items: center;
  }
  .board__skyline {
    position: absolute; inset: 0;
    background: linear-gradient(180deg, rgba(230,220,190,0) 0%, rgba(225,214,182,0.55) 70%, rgba(225,214,182,0.2) 100%);
  }
  .brand {
    position: relative;
    margin-top: 96px;
    display: flex; align-items: center; gap: 10px;
  }
  .brand__mark {
    width: 18px; height: 18px;
    background: var(--gold);
  }
  .brand__name {
    font-family: "Montserrat", sans-serif;
    font-weight: 600;
    font-size: 27px;
    color: var(--ink);
    letter-spacing: -0.3px;
  }
  .collection {
    position: relative;
    margin-top: 8px;
    font-family: "Cinzel", serif;
    font-weight: 500;
    color: var(--gold-deep);
    text-align: center;
    line-height: 0.98;
    font-size: 50px;
  }
  .collection .cap { font-size: 62px; }
  .phone {
    position: absolute;
    left: 60px; top: 283px;
    width: 482px; height: 68px;
    border-radius: 34px;
    background: linear-gradient(180deg, var(--gold-light) 0%, var(--gold) 55%, #a88a22 100%);
    box-shadow: 0 6px 8px -4px rgba(0,0,0,0.35);
    display: flex; align-items: center; justify-content: center; gap: 12px;
  }
  .phone__icon { width: 40px; height: 40px; }
  .phone__number {
    font-family: "Montserrat", sans-serif;
    font-weight: 800;
    font-size: 50px;
    color: var(--black);
    letter-spacing: -0.5px;
    line-height: 1;
  }
  .board__footer {
    height: 70px;
    background: radial-gradient(ellipse at 50% 100%, var(--black-soft) 0%, var(--black) 65%);
    display: flex; align-items: center; justify-content: center;
  }
  .board__web {
    font-family: "Tinos", serif;
    font-size: 21px;
    color: var(--white);
    letter-spacing: 0.4px;
  }
</style>
</head>
<body>
<main class="canvas">
  <section class="board">
    <header class="board__header">
      <h1 class="board__headline">FOR SALE</h1>
    </header>
    <div class="board__rule"></div>
    <div class="board__body">
      <div class="board__skyline" role="img" aria-label="Faint backdrop of town buildings and a clock tower in cream tones"></div>
      <div class="brand">
        <span class="brand__mark"></span>
        <span class="brand__name">Harbour Lane Estates</span>
      </div>
      <h2 class="collection"><span class="cap">T</span>HE <span class="cap">H</span>ARBOUR<br><span class="cap">C</span>OLLECTION</h2>
      <div class="phone">
        <svg class="phone__icon" viewBox="0 0 40 40" aria-hidden="true">
          <path d="M9 5c2-1 4 0 5 2l3 6c1 2 0 3-1 4l-2 2c1 4 5 8 9 10l2-2c1-1 3-2 4-1l6 3c2 1 3 3 2 5l-2 3c-2 2-5 3-8 2C16 36 6 25 4 14c-1-3 0-6 2-8z" fill="#000"/>
          <path d="M22 12a7 7 0 0 1 6 6M23 6a13 13 0 0 1 11 11M24 1a18 18 0 0 1 15 15" stroke="#000" stroke-width="2.6" fill="none" stroke-linecap="round"/>
        </svg>
        <span class="phone__number">178-555-0147</span>
      </div>
    </div>
    <div class="board__rule"></div>
    <footer class="board__footer">
      <span class="board__web">WWW.HARBOURLANEESTATES.CO.UK</span>
    </footer>
  </section>
</main>
</body>
</html>
```